Tax Preparation flyer for LedgerWise Corp.

My Client would like a one page PDF flyer to promote upcoming tax season in Canada. This firm is affordable and all virtual. I have attached a copy of their logo and a word document with the proposed wording for the flyer. Please feel free to change if you have better suggestions.

Target Market(s)

individuals in canada

Colors
0054AA
0677BA
7BADD7
CADEEF
E8F1F8

```html
<!DOCTYPE html>
<html lang="en">
<head>
<meta charset="utf-8">
<title>LedgerWise Corp. – Tax Season Flyer</title>
<link rel="stylesheet" href="https://fonts.googleapis.com/css2?family=Poppins:ital,wght@0,400;0,500;0,600;0,700;0,800;1,600&family=Barlow+Condensed:wght@600&display=swap">
<style>
:root{
  --navy:#0054AA;
  --blue:#0677BA;
  --bright:#1b8fd6;
  --sky:#7BADD7;
  --pale:#CADEEF;
  --mist:#E8F1F8;
  --ink:#222326;
  --cell:#2a2b2e;
  --stage:#d6dce7;
  --white:#ffffff;
}
*{box-sizing:border-box;margin:0;padding:0}
html,body{width:1200px;height:2400px;overflow:hidden;background:var(--stage);font-family:"Poppins",sans-serif;color:var(--ink)}
.flyer{position:absolute;left:50px;top:487px;width:1100px;height:1425px;background:var(--white);box-shadow:0 6px 18px rgba(0,0,0,.25);overflow:hidden}
.abs{position:absolute}
.hero{left:0;top:0;width:1100px;height:600px;background:var(--ink)}
.hero-photo{left:511px;top:0;width:589px;height:480px;background:radial-gradient(ellipse 60% 62% at 62% 52%,#2a9be0 0%,#1f7fc4 32%,#c8202a 58%,rgba(34,35,38,0) 100%)}
.brand{left:66px;top:62px;font-weight:700;font-size:56px;color:var(--white);letter-spacing:-1px;display:flex;align-items:center;gap:14px}
.brand-mark{width:22px;height:22px;background:var(--bright)}
.headline{left:66px;top:252px;color:var(--white)}
.headline .relax{font-weight:800;font-size:94px;line-height:1;color:var(--bright);letter-spacing:1px}
.headline .line{font-weight:500;font-size:60px;line-height:1;margin-top:20px}
.headline .strong{font-weight:800;font-size:62px;line-height:1}
.band{left:70px;top:510px;width:950px;height:166px;display:flex}
.band-left{width:475px;background:var(--navy);display:flex;align-items:center;padding:0 14px 0 16px;gap:12px}
.band-right{flex:1;background:linear-gradient(90deg,var(--blue),var(--bright));padding:18px 16px 0 18px;color:var(--white);font-size:15.5px;line-height:18px}
.years{color:var(--white);text-align:center;font-family:"Barlow Condensed",sans-serif;font-weight:600}
.years .num{font-size:88px;line-height:.85}
.years .cap{font-size:19px;line-height:19px}
.band-left p{color:var(--white);font-size:15px;line-height:17.5px}
.sign{display:inline-flex;align-items:center;gap:4px;font-weight:600;font-size:13px}
.sign i{display:inline-block;width:12px;height:12px;background:#f2d400}
.meet{display:flex;align-items:center;gap:10px;margin-top:14px}
.meet p{font-weight:700;font-size:14.5px;line-height:17px;flex:1}
.meet .sq{width:40px;height:40px;background:var(--sky);border-radius:6px}
.pricing-tab{left:77px;top:738px;width:32px;height:188px;background:var(--ink);color:var(--white);font-weight:700;font-size:22px;letter-spacing:5px;writing-mode:vertical-rl;transform:rotate(180deg);display:flex;align-items:center;justify-content:center}
.price{left:124px;top:734px}
.price .label{font-weight:600;font-size:31px;color:var(--bright);line-height:1;margin-left:10px}
.price .big{font-weight:800;font-size:78px;line-height:1;letter-spacing:1px;margin-top:4px}
.price .add{font-size:19px;margin-left:6px;margin-top:2px}
.price .row{display:flex;align-items:center;gap:18px;margin-top:2px}
.price .small{font-weight:800;font-size:66px;color:var(--bright);line-height:1}
.price .per{font-weight:700;font-size:19px;line-height:20px}
.notes{left:548px;top:728px;width:490px;font-size:15px;line-height:18px}
.notes p{margin-bottom:16px}
.notes .cta{color:var(--bright);font-size:17px}
.notes .cta b{font-weight:700}
.illus{left:60px;top:966px;width:196px;height:190px;background:linear-gradient(135deg,var(--mist),var(--sky));border-radius:8px}
.teaser{left:265px;top:996px;width:180px;font-weight:600;font-style:italic;color:var(--bright);font-size:16.5px;line-height:19px}
.story{left:66px;top:1174px;width:360px;font-size:14px;line-height:16px}
.story .lead{font-weight:700;font-size:16.5px;line-height:19px;margin-bottom:6px}
.story h4{font-weight:600;font-size:14px;margin-top:6px}
.story p{margin-bottom:10px}
.costs{left:458px;top:985px;width:568px}
.costs .title{height:54px;background:var(--navy);color:var(--white);font-weight:700;font-size:17px;letter-spacing:5px;display:flex;align-items:center;justify-content:center;border-radius:6px 6px 0 0}
.costs table{border-collapse:separate;border-spacing:4px;margin:4px -4px 0;width:calc(100% + 8px);table-layout:fixed}
.costs th{background:var(--blue);color:var(--white);font-weight:400;font-size:15px;line-height:18px;height:48px;white-space:nowrap}
.costs th:first-child{background:var(--bright)}
.costs td{background:var(--cell);color:var(--white);font-size:16px;line-height:19px;text-align:center;height:92px}
.costs td.premium{background:#141414}
.costs sup{font-size:9px}
.call{left:460px;top:1228px;width:566px;display:flex;align-items:center;gap:6px}
.call h3{font-weight:700;font-size:34px;letter-spacing:6px;color:var(--bright);white-space:nowrap}
.call hr{flex:1;border:0;border-top:2px solid var(--ink)}
.contacts{left:466px;top:1280px;width:560px;display:flex;justify-content:space-between;font-size:20px;font-weight:500}
.contacts span{display:flex;align-items:center;gap:8px}
.web{left:460px;top:1318px;width:564px;height:50px;background:var(--bright);color:var(--white);font-weight:600;font-size:28px;letter-spacing:5px;display:flex;align-items:center;justify-content:center;border-radius:6px;box-shadow:0 4px 8px rgba(0,0,0,.25)}
</style>
</head>
<body>
<main class="flyer">
  <section class="abs hero"></section>
  <div class="abs hero-photo" role="img" aria-label="Smiling woman in a blue sweater and white sunglasses holding a fan of banknotes in front of a red maple leaf, with bills flying around"></div>

  <div class="abs brand"><span>LedgerWise Corp.</span><span class="brand-mark"></span></div>

  <h1 class="abs headline">
    <div class="relax">RELAX,</div>
    <div class="line">WE’VE GOT YOUR</div>
    <div class="strong">TAXES COVERED!</div>
  </h1>

  <section class="abs band">
    <div class="band-left">
      <div class="years"><div class="num">20</div><div class="cap">YEARS OF<br>EXPERIENCE</div></div>
      <p>Our tax preparers have over worked both in public accounting firms as well as specialized tax. Our tax services are virtual, so you don’t have to take the time for a personal visit. We take care of everything and can access all your tax slips from Revenue Agency website directly into our tax software. All signing is done via <span class="sign"><i></i>Quillora</span></p>
    </div>
    <div class="band-right">
      <p>You can fill and submit the appropriate forms, along with all your other documents, in our secure client portal. It’s important that we understand your situation and any changes in your situation from the past year.</p>
      <div class="meet">
        <p>If you have a complex tax situation and would like to discuss it, we can meet in virtually over Meetnook or Callvale</p>
        <span class="sq"></span>
      </div>
    </div>
  </section>

  <div class="abs pricing-tab">PRICING</div>
  <section class="abs price">
    <div class="label">PERSONAL TAX RETURN</div>
    <div class="big">$100.00</div>
    <div class="add">ADD A BUSINESS OR RENTAL SCHEDULE</div>
    <div class="row"><span class="small">$125</span><span class="per">PER BUSINESS OR<br>RENTAL PROPERTY</span></div>
  </section>

  <section class="abs notes">
    <p>More complex tax returns will be assessed based on the complexity of the return and you will be advised before we start.</p>
    <p>Did you fall behind in filing your income tax save 20% when you file 3 or more years with us. We can do back to 2012 for filing of tax returns.</p>
    <p style="margin-bottom:2px">If you expect a refund, the earlier you file the sooner you will receive your refund. Our average turn around time prior to April is a couple of days.</p>
    <p class="cta">TODAY SO YOU CAN START TO <b>BREATHE EASY.</b></p>
  </section>

  <div class="abs illus" role="img" aria-label="Isometric illustration of a laptop with charts, documents and a person working on bookkeeping"></div>
  <p class="abs teaser">Imagine having your bookkeeping on auto pilot, with everything always up to date and available at your fingertips. Anytime. Anywhere.</p>

  <section class="abs story">
    <p class="lead">You’ll always know exactly where you stand with your cash flow—how much you have, owe, are owed, and have made.</p>
    <h4>How will you feel?</h4>
    <p>Calm, relaxed, and able to make good business decisions. And you’ll have more time to work on your business. In short, you’ll be able to breathe easy.</p>
    <h4>Sound too good to be true?</h4>
    <p>That’s exactly how our clients feel once all their bookkeeping stresses are gone.</p>
  </section>

  <section class="abs costs">
    <div class="title">BOOKKEEPING &amp; ACCOUNTING COSTS</div>
    <table>
      <tr><th>DIY</th><th>Part-Time<br>Bookkeeper</th><th>Full-Time<br>Bookkeeper</th><th>FullOutsources<br>Accounting Team</th></tr>
      <tr><td>No added<br>financial<br>cost</td><td>$3,500-4,500<br>Per month +<br>benefits<sup>(1)</sup></td><td>$4,800-5,500<br>Per month +<br>benefits<sup>(2)</sup></td><td class="premium">$5,000+<sup>(4)</sup></td></tr>
    </table>
  </section>

  <div class="abs call"><h3>CALL US TODAY!</h3><hr></div>
  <div class="abs contacts">
    <span><svg width="18" height="18" viewBox="0 0 18 18"><circle cx="9" cy="9" r="9" fill="#1b8fd6"/><path d="M6 4.5l2 2-1 1.2c.6 1.4 1.6 2.4 3 3l1.2-1 2 2-1.2 1.5C9 13 5 9 4.8 5.7z" fill="#fff"/></svg>555 0142 0199</span>
    <span><svg width="18" height="18" viewBox="0 0 18 18"><circle cx="9" cy="9" r="9" fill="#1b8fd6"/><rect x="4.5" y="6" width="9" height="6.5" fill="#fff"/><path d="M4.5 6l4.5 3.5L13.5 6" stroke="#1b8fd6" fill="none"/></svg>info@ledgerwisecorp.com</span>
  </div>
  <div class="abs web">www.ledgerwisecorp.com</div>
</main>
</body>
</html>
```